Company document Header needed

Using our current logo, I need a Designer to create a header for use on our company documents. This header will include our business address, phone, fax, website address
Updates

Project Deadline Extended
Reason: Dear designers, I am so pleased with the many different options that have been presented, that I wish to purchase several of them from a few different designers. I will get with the art bazaar folks and figure out what is the best way to do this. In the meantime, I am extending the deadline to allow for a few edits such as our phone number and such. thanks to you all for your excellent work. MB

Designers,

Please take a look and edit any of your submissions that have incorrect info on them:  the correct info is below:

Business name is: Tor Vale, Inc.

website address is:  www.torvale-example.com

Office #:  (855) TorVale2  

Fax#:  (858) 561-2947  (generally I do not intend to need this on any materials unless it balances a look)

email:  info@torvale-example.com

Address:  612 Harbor Rd. suite 2240  San Diego, CA  92113

Thanks!

Industry/Entity Type

Business

```html
<!DOCTYPE html>
<html lang="en">
<head>
<meta charset="utf-8">
<title>Tor Vale, Inc. — Letterhead</title>
<link rel="stylesheet" href="https://fonts.googleapis.com/css2?family=Oswald:wght@700&display=swap">
<style>
  :root {
    --paper: #ffffff;
    --navy-deep: #06163f;
    --navy: #0b2c6b;
    --blue-mid: #1d5aa8;
    --blue-light: #7fb3e6;
    --rule-dark: #0a2a66;
    --rule-light: #5b8fd0;
  }
  html, body {
    margin: 0;
    padding: 0;
    overflow: hidden;
    background: var(--paper);
  }
  .letterhead {
    position: relative;
    width: 847px;
    height: 1200px;
    background: var(--paper);
    overflow: hidden;
  }
  .header-band {
    position: absolute;
    left: 0;
    top: 14px;
    width: 847px;
    height: 133px;
    display: block;
  }
  .brand {
    position: absolute;
    left: 16px;
    top: 94px;
    display: flex;
    align-items: center;
    gap: 10px;
  }
  .brand-mark {
    width: 14px;
    height: 14px;
    background: var(--navy);
  }
  .brand-name {
    font-family: "Oswald", "Arial Narrow", sans-serif;
    font-weight: 700;
    font-size: 34px;
    line-height: 1;
    letter-spacing: 1px;
    color: var(--navy);
    margin: 0;
  }
  .rule {
    position: absolute;
    left: 0;
    width: 847px;
  }
  .rule-dark {
    top: 152px;
    height: 4px;
    background: var(--rule-dark);
  }
  .rule-light {
    top: 160px;
    height: 2px;
    background: var(--rule-light);
  }
</style>
</head>
<body>
  <main class="letterhead">
    <svg class="header-band" viewBox="0 0 847 133" role="img" aria-label="Navy blue header band with light diagonal streaks">
      <defs>
        <linearGradient id="band-fill" x1="0" y1="0" x2="1" y2="0">
          <stop offset="0" stop-color="#0b2c6b"/>
          <stop offset="0.45" stop-color="#1d5aa8"/>
          <stop offset="0.75" stop-color="#0b2c6b"/>
          <stop offset="1" stop-color="#06163f"/>
        </linearGradient>
        <linearGradient id="streak-fill" x1="0" y1="0" x2="0" y2="1">
          <stop offset="0" stop-color="#ffffff" stop-opacity="0.55"/>
          <stop offset="1" stop-color="#7fb3e6" stop-opacity="0.15"/>
        </linearGradient>
      </defs>
      <rect width="847" height="133" fill="url(#band-fill)"/>
      <polygon points="250,0 300,0 250,133 200,133" fill="url(#streak-fill)"/>
      <polygon points="330,0 350,0 300,133 280,133" fill="url(#streak-fill)" opacity="0.7"/>
      <polygon points="420,0 470,0 420,133 370,133" fill="url(#streak-fill)" opacity="0.5"/>
      <rect x="0" y="96" width="847" height="1.5" fill="#7fb3e6" opacity="0.5"/>
      <polygon points="0,0 215,0 170,133 0,133" fill="#ffffff"/>
    </svg>

    <div class="brand">
      <span class="brand-mark" aria-hidden="true"></span>
      <h1 class="brand-name">TOR VALE</h1>
    </div>

    <div class="rule rule-dark"></div>
    <div class="rule rule-light"></div>
  </main>
</body>
</html>
```